Newspaper ad advertising bathroom adaptations for the less-abled and disabled.

This ad is to really promote bathroom adaptations that are suited to the clients needs, so more care led rather than design led. Important for the ad to be easy to read and easy to understand. Clearly states bathroom conversions from £4,999 to help qualify leads generated from the ad. We are looking to reach out to anyone whose bathroom is becoming more challenging because of mobility issues so we can use our excellent industry knowledge and personal family experience to come up with solutions that really work for the client

Target Market(s)

predominately older people

Industry/Entity Type

Health And Wellness

Font styles to use
Serif

Colors

Designer to choose colors to be used in the design.

Requirements
Must have
• It must have the content that is included in advert i have attached. Use where possible the photos of the actual jobs we've done to make it relatable for the client to see real jobs.
Nice to have
• some added pictures of mobility bathroom equipment including walk-in baths, walk-in showers and wetroom flooring.
Should not have
• anything too heavy on the eye.

```html
<!DOCTYPE html>
<html lang="en">
<head>
<meta charset="utf-8">
<title>Brightwater Adaptations – Adapted Bathroom Ad</title>
<link rel="stylesheet" href="https://fonts.googleapis.com/css2?family=Montserrat:wght@400;600;700;800&family=Encode+Sans+Condensed:wght@400;500;600;700&display=swap">
<style>
:root{
  --navy:#173f73;
  --navy-dark:#123563;
  --teal:#13a59a;
  --orange:#f26f21;
  --grey:#b9babd;
  --panel:#efeff0;
  --badge:#ffffff;
  --badge-edge:#d6d7da;
  --backdrop:#d2d0d3;
  --white:#ffffff;
  --ink:#1d3d6c;
}
*{box-sizing:border-box;margin:0;padding:0}
html,body{width:1200px;height:1200px;overflow:hidden}
body{background:var(--backdrop);font-family:"Encode Sans Condensed",sans-serif;position:relative}
.ad{position:absolute;left:177px;top:0;width:846px;height:1200px;background:var(--white);overflow:hidden}
.hero-art{position:absolute;left:0;top:0;width:846px;height:440px}
.price-badge{position:absolute;left:456px;top:205px;width:206px;height:206px;border-radius:50%;background:var(--navy);border:5px solid var(--teal);color:var(--white);text-align:center;padding-top:16px;font-family:"Encode Sans Condensed",sans-serif;box-shadow:0 8px 8px -6px rgba(0,0,0,.25)}
.price-badge .kicker{font-weight:700;font-size:17px;line-height:18px}
.price-badge .kicker-big{font-family:"Montserrat",sans-serif;font-weight:800;font-size:20px;line-height:22px}
.price-badge .detail{font-size:17px;line-height:21px;font-weight:400}
.price-badge .price{font-weight:700;font-size:52px;line-height:54px;color:var(--orange);letter-spacing:-1px}
.price-badge .price sup{font-size:16px;vertical-align:top;position:relative;top:4px}
.intro{position:absolute;left:28px;top:426px;width:540px}
.intro .question{font-family:"Montserrat",sans-serif;font-weight:800;color:var(--navy);font-size:30.5px;line-height:33px;letter-spacing:-.4px}
.intro .answer{font-family:"Montserrat",sans-serif;font-weight:800;color:var(--orange);font-size:37px;line-height:42px;letter-spacing:-.6px;margin-top:1px}
.intro .strap{font-family:"Montserrat",sans-serif;color:var(--teal);font-size:17.5px;line-height:20px;margin-top:2px}
.intro .promise{font-family:"Montserrat",sans-serif;color:var(--teal);font-size:10.8px;line-height:14px;margin-top:3px}
.rule{position:absolute;left:28px;width:512px;height:1px;background:#e1e1e3}
.services{position:absolute;left:28px;top:592px;width:540px}
.services h2{font-family:"Montserrat",sans-serif;font-weight:800;color:var(--navy);font-size:22.5px;line-height:26px}
.service-cols{display:flex;margin-top:5px}
.service-list{list-style:none;font-size:11.2px;color:var(--ink);line-height:12.4px}
.service-list:first-child{width:281px}
.service-list:last-child{width:270px}
.service-list li{position:relative;padding-left:26px;margin-bottom:7px}
.service-list li::before{content:"";position:absolute;left:8px;top:1px;width:4px;height:8px;border-right:1.6px solid var(--orange);border-bottom:1.6px solid var(--orange);transform:rotate(40deg)}
.audience{position:absolute;left:28px;top:808px;width:512px;text-align:center;font-family:"Montserrat",sans-serif;font-weight:800;color:var(--navy);font-size:21.5px;line-height:29px}
.accreditations{position:absolute;left:28px;top:868px;width:496px;height:94px;background:var(--panel);border-radius:9px;display:flex;justify-content:space-around;align-items:center;padding:0 16px}
.accreditations .mark{width:90px;height:62px;background:var(--badge);border:1px solid var(--badge-edge);border-radius:8px}
.footnote{position:absolute;left:28px;top:968px;font-size:6.6px;color:#333}
.gallery-frame{position:absolute;left:588px;top:378px;width:246px;height:642px;background:var(--orange);clip-path:polygon(0 40px,100% 0,100% 100%,0 600px)}
.gallery-photo{position:absolute;left:598px;width:222px}
.photo-1{top:392px;height:166px;clip-path:polygon(0 26px,100% 0,100% 100%,0 100%);background:linear-gradient(135deg,#dfe0de,#c9cbc8 55%,#e9eae8)}
.photo-2{top:565px;height:130px;background:linear-gradient(135deg,#6f8478,#c9c3b6 50%,#5e7367)}
.photo-3{top:703px;height:130px;background:linear-gradient(160deg,#6a7f74,#e8e7e4 55%,#cfcbc4)}
.photo-4{top:840px;height:171px;clip-path:polygon(0 0,100% 0,100% 100%,0 83%);background:linear-gradient(180deg,#6c8277,#dcd8d2 60%,#9b8a78)}
.footer-art{position:absolute;left:0;top:975px;width:846px;height:225px}
.brand-box{position:absolute;left:35px;top:1039px;width:368px;height:98px;border:4px solid var(--orange);border-radius:14px;background:#f0f0f1;display:flex;align-items:center;padding-left:22px;gap:16px}
.brand-dot{width:40px;height:40px;border-radius:50%;background:var(--teal);flex:none}
.brand-name{font-family:"Montserrat",sans-serif;font-weight:800;color:var(--navy);font-size:27px;line-height:30px}
.cta{position:absolute;left:434px;top:1038px;width:378px;color:var(--white);font-family:"Montserrat",sans-serif;font-weight:700;font-size:17.4px;line-height:19px;letter-spacing:.8px;text-align:center}
.cta-rule{position:absolute;left:436px;top:1084px;width:372px;height:2px;background:var(--teal)}
.phone{position:absolute;left:432px;top:1090px;width:384px;font-family:"Encode Sans Condensed",sans-serif;font-weight:700;font-size:52px;line-height:56px;color:var(--orange);text-align:center;letter-spacing:1px}
.web-line{position:absolute;left:0;top:1155px;width:846px;display:flex;align-items:center;gap:12px}
.web-line .bar{flex:1;height:4px;background:var(--teal)}
.web-line .links{font-family:"Encode Sans Condensed",sans-serif;font-weight:600;font-size:20px;color:var(--teal);white-space:nowrap}
</style>
</head>
<body>
<main class="ad">
  <svg class="hero-art" viewBox="0 0 846 440">
    <defs>
      <linearGradient id="heroTone" x1="0" y1="0" x2="1" y2="1">
        <stop offset="0" stop-color="#5f7668"/>
        <stop offset=".45" stop-color="#c7b9a6"/>
        <stop offset=".75" stop-color="#e9e6e2"/>
        <stop offset="1" stop-color="#7b8d80"/>
      </linearGradient>
    </defs>
    <path role="img" aria-label="Photo of a finished adapted bathroom with walk-in shower, toilet and vessel basin against green tiles" d="M0,0H846V330C720,380 600,402 520,404C330,404 180,300 0,232Z" fill="url(#heroTone)"/>
    <path d="M0,232C180,300 330,404 520,404C600,402 720,380 846,330V346C720,396 600,418 520,420C330,420 170,318 0,254Z" fill="var(--navy)"/>
    <path d="M0,254C170,318 330,420 520,420C600,418 720,396 846,346V352C720,404 600,426 520,428C330,428 170,326 0,262Z" fill="var(--grey)"/>
    <path d="M0,262C170,326 300,414 420,428C300,420 150,340 0,296Z" fill="var(--teal)"/>
    <path d="M0,303C80,312 140,330 156,346" fill="none" stroke="var(--orange)" stroke-width="3"/>
  </svg>

  <div class="price-badge">
    <div class="kicker">ADAPTED</div>
    <div class="kicker-big">BATHROOM</div>
    <div class="detail">CONVERSIONS TO HELP<br>WITH YOUR MOBILITY<br>NEEDS FROM</div>
    <div class="price">£4,999<sup>*</sup></div>
  </div>

  <section class="intro">
    <h1 class="question">IS YOUR BATHROOM<br>BECOMING MORE CHALLENGING?</h1>
    <p class="answer">WE HAVE THE SOLUTION...</p>
    <p class="strap">FROM CONCEPT TO CREATION TO COMPLETION. . .</p>
    <p class="promise">we care passionately about installing a quality bathroom that really works for your needs</p>
  </section>

  <div class="rule" style="top:581px"></div>

  <section class="services">
    <h2>WE DO IT ALL</h2>
    <div class="service-cols">
      <ul class="service-list">
        <li>Existing bathroom to wetroom conversions</li>
        <li>Walk-in showers &amp; wetrooms tailored to<br>meet your needs</li>
        <li>Full bathroom mobility enablement</li>
        <li>Free no obligation home assessment</li>
        <li>Full detailed pre-install survey</li>
        <li>Fully project managed dedicated installation team</li>
        <li>Full insurance backed guarantee on all adaptations</li>
        <li>All tiling, electrics, plumbing etc carried out</li>
      </ul>
      <ul class="service-list">
        <li>Bathing enabling equipment</li>
        <li>Work closely with occupational therapists</li>
        <li>Anti-slip safety flooring</li>
        <li>Maintenance free shower panelling</li>
        <li>Walk-in easy access baths</li>
        <li>Specialist wash &amp; dry toilets</li>
        <li>Fully accredited to HomeCare Trust, the Bathing Trades Guild and the Fair Work Association</li>
      </ul>
    </div>
  </section>

  <div class="rule" style="top:795px"></div>

  <h2 class="audience">BATHROOM ADAPTATIONS FOR THE<br>ELDERLY, DISABLED AND LESS ABLED</h2>

  <div class="accreditations">
    <span class="mark" role="img" aria-label="Accreditation badge"></span>
    <span class="mark" role="img" aria-label="Trade association badge"></span>
    <span class="mark" role="img" aria-label="Approved code badge"></span>
    <span class="mark" role="img" aria-label="Trades listing badge"></span>
  </div>

  <p class="footnote">*Pricing is a guide only and could vary dependant on home survey and work involved</p>

  <div class="gallery-frame"></div>
  <div class="gallery-photo photo-1" role="img" aria-label="Photo of a walk-in shower with fold-down shower seat and handrail"></div>
  <div class="gallery-photo photo-2" role="img" aria-label="Photo of a low-level shower tray with glass screen"></div>
  <div class="gallery-photo photo-3" role="img" aria-label="Photo of a vessel basin on a floating vanity shelf"></div>
  <div class="gallery-photo photo-4" role="img" aria-label="Photo of a wall-hung toilet against green tiles"></div>

  <svg class="footer-art" viewBox="0 0 846 225" aria-hidden="true">
    <path d="M0,38C250,5 500,0 846,40V225H0Z" fill="var(--teal)"/>
    <path d="M0,56C260,25 560,22 846,70V225H0Z" fill="var(--navy)"/>
  </svg>

  <div class="brand-box">
    <span class="brand-dot"></span>
    <span class="brand-name">Brightwater<br>Adaptations</span>
  </div>

  <p class="cta">CALL TODAY FOR A NO OBLIGATION<br>HOME ASSESSMENT OR A BROCHURE</p>
  <div class="cta-rule"></div>
  <p class="phone">01632 960 418</p>

  <div class="web-line">
    <span class="bar"></span>
    <span class="links">enquiries@brightwateradaptations.com / www.brightwateradaptations.com</span>
    <span class="bar"></span>
  </div>
</main>
</body>
</html>
```